Online hair business needs a Glam Web and Logo design*

I am launching an online business selling Brazillian Hair Weave. My business name is ZolaT Tresses and I would love a logo with a glamorous female image, maybe a silhouette, with long wavy hair and I would like the initials ZTT or ZT somewhere in the logo on the top, bottom or as jewelry (earrings/necklace). It does not have to be a female image, but it needs to be eye-catching.

Industry/Entity Type

Hair And Beauty

Logo Text

ZolaT Tresses

Number of Pages Required

1 page

Font styles to use
Sans Serif

Colors

Designer to choose colors to be used in the design.

Requirements
Nice to have
• I need to display the hair to sell, but would also like to display models or images with the hair installed. I also need to have FAQ's and would like to be able to add some videos.

```html
<!DOCTYPE html>
<html lang="en">
<head>
<meta charset="utf-8">
<title>ZolaT Tresses – Brazilian Hair</title>
<link href="https://fonts.googleapis.com/css2?family=Dancing+Script:wght@500&family=Lato:wght@400;700&family=Alegreya:ital,wght@1,400;1,500&family=Montserrat:wght@400;500&family=Quicksand:wght@500&display=swap" rel="stylesheet">
<style>
:root{
  --brown:#6b2a1f;
  --red:#c0252e;
  --blush:#fce9e6;
  --gold:#a8770f;
  --charcoal:#4d4945;
  --nav-active:#8f5246;
  --grey-bg:#f4f4f4;
  --text:#3c3c3c;
  --muted:#8d8d8d;
  --line:#bdbdbd;
  --bar:#7a2e20;
}
*{margin:0;padding:0;box-sizing:border-box}
html,body{width:1200px;height:2539px;overflow:hidden;background:#fff}
body{position:relative;font-family:"Montserrat",sans-serif;color:var(--text)}
.abs{position:absolute}
.body-copy{font-family:"Quicksand",sans-serif;font-weight:500}
.script{font-family:"Dancing Script",cursive}
.serif-title{font-family:"Alegreya",serif;font-style:italic;font-weight:400;color:var(--brown)}
.btn{position:absolute;display:flex;align-items:center;justify-content:center;gap:12px;color:#fff;font-family:"Lato",sans-serif;font-weight:700;font-size:17px;text-transform:uppercase}
.btn svg{width:16px;height:12px}

/* header */
.site-header{left:0;top:0;width:1200px;height:102px;background:#fff}
.brand{left:76px;top:22px;display:flex;align-items:center;gap:12px}
.brand-dot{width:44px;height:44px;border-radius:50%;background:var(--brown)}
.brand-name{font-family:"Montserrat",sans-serif;font-weight:500;font-size:24px;color:var(--brown)}
.demo{left:626px;top:28px;display:flex;gap:12px;align-items:center}
.demo small{display:block;font-size:13px;color:var(--text)}
.demo strong{display:block;font-family:"Lato",sans-serif;font-weight:700;font-size:25px;color:var(--brown);margin-top:2px}
.header-rule{left:906px;top:30px;width:1px;height:48px;background:#e2e2e2}
.social-ring{top:29px;width:44px;height:44px;border-radius:50%;border:2px solid #d8d8d8}
.social-ring.filled{background:#d8d8d8}

/* nav */
.main-nav{left:0;top:102px;width:1200px;height:55px;background:#fdf8f7;border-top:1px solid #eee;box-shadow:0 2px 4px rgba(0,0,0,.12)}
.nav-item{top:0;height:55px;line-height:55px;font-size:15px;color:#8a8a8a;transform:translateX(-50%)}
.nav-item.active{left:176px;width:104px;transform:none;text-align:center;background:var(--nav-active);color:#fff}

/* hero */
.hero{left:0;top:157px;width:1200px;height:540px;background:var(--blush)}
.hero-photo{right:0;top:0;width:506px;height:540px;background:radial-gradient(ellipse at 55% 45%,#f0d2b4 0%,#e9c9a6 35%,#f6e4d6 70%,var(--blush) 100%)}
.hero-kicker{left:76px;top:92px;font-size:112px;font-weight:500;color:#4a4341;line-height:1}
.hero-line2{left:78px;top:216px;font-family:"Lato",sans-serif;font-weight:400;font-size:62px;color:var(--red);line-height:1}
.hero-line3{left:79px;top:285px;font-family:"Lato",sans-serif;font-weight:700;font-size:42px;color:var(--brown);line-height:1}
.hero-rule{left:78px;top:361px;width:166px;height:2px;background:#4a4341}

/* products */
.section-title{left:0;width:1200px;text-align:center;font-size:52px}
.product-card{top:831px;width:313px;height:344px;overflow:hidden}
.product-card .photo{position:absolute;inset:0}
.product-card .label{position:absolute;left:0;top:84px;width:100%;text-align:center;color:#fff;font-size:25px;line-height:1.2}
.product-card .dash{position:absolute;left:50px;right:50px;top:180px;border-top:2px dashed #fff}
.product-card .shop{position:absolute;left:50%;top:210px;transform:translateX(-50%);height:40px;padding:0 12px;line-height:38px;font-size:17px;border:2px solid #fff;background:#fff;color:#333;white-space:nowrap}
.product-card .shop.ghost{background:transparent;color:#fff}
.slider-arrow{top:1114px;width:62px;height:61px;background:#cfcfcf;display:flex;align-items:center;justify-content:center}

/* about */
.about{left:0;top:1227px;width:1200px;height:356px;background:var(--grey-bg)}
.about-copy{left:170px;top:1371px;width:860px;text-align:center;font-size:13.5px;line-height:23px;color:var(--muted)}

/* faq */
.faq-sub{left:0;top:1726px;width:1200px;text-align:center;font-size:17px;color:#444}
.faq-q{left:106px;font-family:"Alegreya",serif;font-style:italic;font-weight:500;font-size:18px;color:#222;white-space:nowrap}
.faq-rule{left:78px;width:635px;height:2px;background:var(--line)}
.faq-open-title{left:106px;top:1886px;font-family:"Alegreya",serif;font-style:italic;font-size:18px;color:var(--brown)}
.faq-open-copy{left:106px;top:1914px;font-size:13px;line-height:26px;color:#555;white-space:nowrap}
.read-more{left:604px;top:1940px;font-size:13px;line-height:26px;color:#222;text-decoration:underline;white-space:nowrap}
.faq-divider{left:735px;top:1778px;width:2px;height:296px;background:#ddd}
.questions-title{left:762px;top:1815px;font-size:28px}
.questions-copy{left:760px;top:1858px;width:360px;font-size:13.5px;line-height:23px;color:#555}

/* footer */
.site-footer{left:0;top:2138px;width:1200px;height:334px;background:linear-gradient(180deg,#f3ddd4 0%,#efd9d2 50%,#e6d3cf 100%)}
.footer-head{top:2190px;font-family:"Alegreya",serif;font-style:italic;font-weight:400;font-size:24px;color:var(--brown)}
.footer-links{top:2232px;list-style:none;font-size:13.5px;line-height:29.5px;color:#333}
.footer-links .faint{color:#999}
.footer-sub{font-family:"Alegreya",serif;font-style:italic;font-weight:500;font-size:17px;color:#222}
.footer-text{font-size:13.5px;line-height:20px;color:#333}
.email{left:606px;top:2263px;width:249px;height:49px;background:#fff;border:1px solid #ddd;font-size:13px;color:#bbb;padding:16px 0 0 14px}
.social-square{top:2387px;width:29px;height:29px;border:1px solid #8a6a62}
.social-square.filled{background:var(--brown);border-color:var(--brown)}
.bottom-bar{left:0;top:2472px;width:1200px;height:67px;background:var(--bar);text-align:center;line-height:67px;font-size:14px;color:#d86e55}
.bottom-bar b{font-family:"Alegreya",serif;font-style:italic;font-weight:500;color:#fff;font-size:16px}
</style>
</head>
<body>

<header class="abs site-header">
  <div class="abs brand"><span class="brand-dot"></span><span class="brand-name">ZolaT Tresses</span></div>
  <div class="abs demo">
    <svg width="42" height="42" viewBox="0 0 24 24" fill="none" stroke="#c0252e" stroke-width="1.6"><path d="M5 3h4l2 5-2.5 1.5a11 11 0 0 0 6 6L16 13l5 2v4a2 2 0 0 1-2 2A16 16 0 0 1 3 5a2 2 0 0 1 2-2z"/><path d="M14 3a7 7 0 0 1 7 7M14 6.5a3.5 3.5 0 0 1 3.5 3.5"/></svg>
    <div><small>GET A FREE DEMO</small><strong>(123) 456-7890</strong></div>
  </div>
  <span class="abs header-rule"></span>
  <span class="abs social-ring filled" style="left:931px"></span>
  <span class="abs social-ring" style="left:982px"></span>
  <span class="abs social-ring" style="left:1033px"></span>
  <span class="abs social-ring" style="left:1080px"></span>
</header>

<nav class="abs main-nav">
  <span class="abs nav-item active">HOME</span>
  <span class="abs nav-item" style="left:401px">ABOUT US</span>
  <span class="abs nav-item" style="left:596px">PRODUCTS</span>
  <span class="abs nav-item" style="left:767px">FAQ</span>
  <span class="abs nav-item" style="left:945px">CONTACT US</span>
</nav>

<section class="abs hero">
  <div class="abs hero-photo" role="img" aria-label="Model with long wavy blonde hair"></div>
  <h1>
    <span class="abs hero-kicker script">Get Everything</span>
    <span class="abs hero-line2">YOU NEED FOR</span>
    <span class="abs hero-line3">ZolaT Tresses</span>
  </h1>
  <span class="abs hero-rule"></span>
  <a class="btn" style="left:78px;top:391px;width:186px;height:52px;background:var(--charcoal)">Find out more <svg viewBox="0 0 16 12"><path d="M0 6h11M9 1l6 5-6 5z" stroke="#fff" fill="#fff" stroke-width="2"/></svg></a>
  <a class="btn" style="left:276px;top:391px;width:228px;height:52px;background:var(--gold)">View all products <svg viewBox="0 0 16 12"><path d="M0 6h11M9 1l6 5-6 5z" stroke="#fff" fill="#fff" stroke-width="2"/></svg></a>
</section>

<h2 class="abs section-title serif-title" style="top:748px">Our Products</h2>

<article class="abs product-card" style="left:130px">
  <div class="photo" role="img" aria-label="Model beside bundles of wavy hair" style="background:linear-gradient(90deg,#5e3a36 0%,#6d403a 50%,#8a584f 100%)"></div>
  <div class="label">Product<br>Name</div><span class="dash"></span><span class="shop ghost">SHOP NOW</span>
</article>
<article class="abs product-card" style="left:444px">
  <div class="photo" role="img" aria-label="Curly black lace frontal hair piece" style="background:radial-gradient(ellipse at 50% 55%,#2b2b2b,#3e3e3e 70%,#444)"></div>
  <div class="label">Product<br>Name</div><span class="dash"></span><span class="shop">SHOP NOW</span>
</article>
<article class="abs product-card" style="left:757px">
  <div class="photo" role="img" aria-label="Packaged bundle of auburn hair" style="background:linear-gradient(180deg,#8f5a4e,#9a6152 50%,#a36a58)"></div>
  <div class="label">Product<br>Name</div><span class="dash"></span><span class="shop">SHOP NOW</span>
</article>
<span class="abs slider-arrow" style="left:58px"><svg width="20" height="30" viewBox="0 0 20 30"><path d="M16 2L4 15l12 13" stroke="#fff" stroke-width="3" fill="none"/></svg></span>
<span class="abs slider-arrow" style="left:1080px"><svg width="20" height="30" viewBox="0 0 20 30"><path d="M4 2l12 13L4 28" stroke="#fff" stroke-width="3" fill="none"/></svg></span>

<section class="abs about"></section>
<h2 class="abs section-title serif-title" style="top:1290px">About Us</h2>
<p class="abs about-copy body-copy">Lorem Ipsum is simply dummy text of the printing and typesetting industry. Lorem Ipsum has been the industry's standard dummy<br>text ever since the 1500s, when an unknown printer took a galley of type and scrambled it to make a type specimen book.It has<br>survived not only five centuries, but also the leap into electronic typesetting, remaining essentially unchanged.</p>
<a class="btn" style="left:506px;top:1458px;width:188px;height:50px;background:var(--charcoal)">Find out more <svg viewBox="0 0 16 12"><path d="M0 6h11M9 1l6 5-6 5z" stroke="#fff" fill="#fff" stroke-width="2"/></svg></a>

<h2 class="abs section-title serif-title" style="top:1645px">Faq's</h2>
<p class="abs faq-sub body-copy">Below is a list of frequently asked questions to help you understand how this works.</p>
<p class="abs faq-q" style="top:1805px">Lorem Ipsum is simply dummy text of the printing and typesetting industry?</p>
<span class="abs faq-rule" style="top:1850px"></span>
<p class="abs faq-open-title">How are you able to offer these Auction?</p>
<p class="abs faq-open-copy body-copy">Lorem Ipsum is simply dummy text of the printing and typesetting industry. Lorem Ipsum<br>has been the industry's standard dummy text ever since the 1500.</p>
<a class="abs read-more">READ MORE</a>
<span class="abs faq-rule" style="top:1997px"></span>
<p class="abs faq-q" style="top:2013px">Lorem Ipsum is simply dummy text of the printing and typesetting industry?</p>
<span class="abs faq-divider"></span>
<h3 class="abs questions-title serif-title">Questions?</h3>
<p class="abs questions-copy body-copy">Lorem Ipsum is simply dummy text of the printing and typesetting industry. Lorem Ipsum has been the industry's standard dummy text ever since the 1500s</p>
<a class="btn" style="left:757px;top:1947px;width:228px;height:51px;background:var(--charcoal)">Contact us today <svg viewBox="0 0 16 12"><path d="M0 6h11M9 1l6 5-6 5z" stroke="#fff" fill="#fff" stroke-width="2"/></svg></a>

<footer class="abs site-footer" role="img" aria-label="Soft pink city skyline backdrop"></footer>
<h4 class="abs footer-head" style="left:80px">Help</h4>
<ul class="abs footer-links body-copy" style="left:80px">
  <li>Help Center</li><li>Contact Customer Care</li><li>Shipping</li><li>Track Order</li><li>Returns</li><li class="faint">Warranty Info</li><li>Size &amp; Buying Guides</li>
</ul>
<h4 class="abs footer-head" style="left:342px">About</h4>
<ul class="abs footer-links body-copy" style="left:342px;top:2235px;line-height:32.5px">
  <li>Home</li><li>About US</li><li>Featured Products</li><li>Blogs/News</li><li>Contact Us</li>
</ul>
<h4 class="abs footer-head" style="left:606px">Newsletter</h4>
<p class="abs footer-text body-copy" style="left:606px;top:2231px">Subscribe to Our Newsletter</p>
<div class="abs email body-copy">E-Mail</div>
<a class="btn" style="left:604px;top:2319px;width:198px;height:51px;background:var(--charcoal)">Subscribe now <svg viewBox="0 0 16 12"><path d="M0 6h11M9 1l6 5-6 5z" stroke="#fff" fill="#fff" stroke-width="2"/></svg></a>
<h4 class="abs footer-head" style="left:872px">Follow Us</h4>
<p class="abs footer-sub" style="left:872px;top:2234px">Our Locations</p>
<p class="abs footer-text body-copy" style="left:872px;top:2261px">123, Lorem ipsum dummy text,<br>Country-123456.</p>
<p class="abs footer-sub" style="left:872px;top:2322px">Phone</p>
<p class="abs footer-text body-copy" style="left:872px;top:2350px">(123) 456-7890</p>
<span class="abs social-square filled" style="left:870px"></span>
<span class="abs social-square" style="left:911px"></span>
<span class="abs social-square" style="left:951px"></span>
<span class="abs social-square" style="left:992px"></span>
<span class="abs social-square" style="left:1033px"></span>

<div class="abs bottom-bar">© <b>ZTT - ZolaT Tresses - 2018.</b> All Rights Reserved.</div>

</body>
</html>
```